Business Card for Makeup Artist

I need a business card designed for my makeup and hair artistry business which is primarily events and weddings focused. The card needs to be sleek, simple, stylish and appealing to women. I would prefer a white background but open to suggestions also. I also love the marble background look. I have attached some example pics. It needs to be a double sided card with logo and/or design on one side and contact details in the centre of the card on the other side. NO LOGO ON BACK. Examples attached.

Target Market(s)

Females age 14-55

Industry/Entity Type

Business

Contact Information for Business Card

Nora Vint
Principal Makeup Artist
P: 0413 925 214
E: nora@lumirabeauty.com.au
W: www.lumirabeauty.com.au

Requirements
Should not have
• No yellow, green, red or blue in the design.

```html
<!DOCTYPE html>
<html lang="en">
<head>
<meta charset="UTF-8">
<title>Lumira Makeup Artistry – Business Card</title>
<link href="https://fonts.googleapis.com/css2?family=Quicksand:wght@300;400&family=Satisfy&display=swap" rel="stylesheet">
<style>
  :root {
    --backdrop: #3a3a3c;
    --card-black: #141414;
    --marble-light: #f4f5f8;
    --marble-mid: #d9dde5;
    --marble-vein: #aab2c2;
    --gold-dark: #a7761c;
    --gold-light: #f3d35a;
    --ink-white: #f2f2f2;
    --ink-grey: #8c8c8f;
    --ink-pink: #e0559e;
  }
  * { margin: 0; padding: 0; box-sizing: border-box; }
  html, body {
    width: 1200px;
    height: 800px;
    overflow: hidden;
    background: var(--backdrop);
  }
  .card-set {
    width: 1200px;
    height: 800px;
    display: flex;
    align-items: center;
    justify-content: center;
    gap: 60px;
  }
  .card {
    position: relative;
    width: 520px;
    height: 318px;
    border-radius: 3px;
    overflow: hidden;
    box-shadow: 0 10px 28px rgba(0, 0, 0, 0.45);
  }

  /* Front */
  .card--front {
    display: flex;
    align-items: center;
    justify-content: center;
  }
  .marble-surface {
    position: absolute;
    inset: 0;
    background:
      linear-gradient(125deg, transparent 30%, rgba(170, 178, 194, 0.35) 38%, transparent 46%),
      linear-gradient(160deg, transparent 55%, rgba(170, 178, 194, 0.3) 62%, transparent 70%),
      radial-gradient(ellipse at 30% 40%, var(--marble-light) 0%, var(--marble-mid) 80%);
  }
  .name-plate {
    position: relative;
    width: 250px;
    padding: 4px;
    background: linear-gradient(135deg, var(--gold-dark), var(--gold-light) 45%, var(--gold-dark) 70%, var(--gold-light));
  }
  .name-plate__inner {
    background: var(--card-black);
    padding: 16px 14px 18px;
    text-align: center;
  }
  .holder-name {
    font-family: "Satisfy", cursive;
    font-size: 36px;
    line-height: 1.1;
    color: var(--ink-white);
  }
  .holder-title {
    margin-top: 6px;
    font-family: "Quicksand", sans-serif;
    font-weight: 400;
    font-size: 15px;
    letter-spacing: 0.5px;
    color: var(--ink-white);
  }

  /* Back */
  .card--back {
    background: var(--card-black);
    padding: 70px 0 0 150px;
    font-family: "Quicksand", sans-serif;
  }
  .brand-name {
    font-weight: 400;
    font-size: 34px;
    line-height: 1;
    color: var(--ink-grey);
  }
  .brand-sub {
    margin-top: 4px;
    font-weight: 400;
    font-size: 11px;
    letter-spacing: 1.5px;
    color: var(--ink-grey);
  }
  .contact-list {
    list-style: none;
    margin-top: 20px;
  }
  .contact-list li {
    font-weight: 300;
    font-size: 15px;
    line-height: 1.75;
    color: var(--ink-grey);
  }
  .contact-list .contact-phone {
    color: var(--ink-pink);
    font-size: 17px;
  }
</style>
</head>
<body>
  <main class="card-set">
    <section class="card card--front">
      <div class="marble-surface" role="img" aria-label="White and grey veined marble texture"></div>
      <div class="name-plate">
        <div class="name-plate__inner">
          <p class="holder-name">Nora Vint</p>
          <p class="holder-title">Principal Makeup Artist</p>
        </div>
      </div>
    </section>

    <section class="card card--back">
      <p class="brand-name">Lumira</p>
      <p class="brand-sub">MAKEUP ARTISTRY</p>
      <ul class="contact-list">
        <li class="contact-phone">0413 925 214</li>
        <li class="contact-email">nora@lumirabeauty.com.au</li>
        <li class="contact-web">www.lumirabeauty.com.au</li>
      </ul>
    </section>
  </main>
</body>
</html>
```